Construction Contractor
Bayt Nuwaris
Professional
Fahad Omar Qurashi
Owner
Rawda Street P.O.Box 483920 Jeddah 24719 Saudi Arabia
baytnuwaris@mailbox-example.com
We need Logo to be in the middle and company name under the logo

```html
<!DOCTYPE html>
<html lang="en">
<head>
<meta charset="utf-8">
<title>Bayt Nuwaris — Business Card</title>
<link rel="stylesheet" href="https://fonts.googleapis.com/css2?family=Open+Sans:ital,wght@0,400;0,600;1,400&family=Montserrat:wght@800&display=swap">
<style>
  :root {
    --backdrop: #e9e5df;
    --card: #ffffff;
    --brown: #5a3d24;
    --gold: #d2b36f;
    --gold-dark: #b8964f;
    --ink: #2b2b2b;
    --muted: #6c6c6c;
    --faint: #9a9a9a;
  }
  * { margin: 0; padding: 0; box-sizing: border-box; }
  html, body { width: 1200px; height: 900px; overflow: hidden; }
  body {
    background: var(--backdrop);
    font-family: "Open Sans", sans-serif;
    position: relative;
  }
  .card {
    position: absolute;
    left: 320px;
    width: 560px;
    height: 320px;
    background: var(--card);
    overflow: hidden;
    box-shadow: 0 6px 18px rgba(0,0,0,0.18);
  }
  .card--back { top: 80px; }
  .card--front { top: 480px; }

  .edge { position: absolute; top: 0; height: 100%; }
  .edge--left { left: 0; width: 40px; }
  .edge--right { right: 0; width: 56px; }

  .brand {
    display: flex;
    flex-direction: column;
    align-items: center;
    font-family: "Montserrat", sans-serif;
    font-weight: 800;
    color: var(--brown);
    text-transform: uppercase;
    letter-spacing: 0.5px;
    white-space: nowrap;
    line-height: 1;
  }
  .brand__mark { background: var(--brown); }

  .card--back .brand {
    position: absolute;
    left: 50%;
    top: 50%;
    transform: translate(-50%, -50%);
    font-size: 30px;
    gap: 14px;
  }
  .card--back .brand__mark { width: 56px; height: 56px; }

  .card--front .brand {
    position: absolute;
    left: 34px;
    top: 36px;
    font-size: 22px;
    gap: 10px;
  }
  .card--front .brand__mark { width: 40px; height: 40px; }

  .person {
    position: absolute;
    right: 96px;
    top: 118px;
    text-align: right;
  }
  .person__name { font-size: 21px; color: var(--ink); font-weight: 400; }
  .person__role { font-size: 12px; color: var(--muted); margin-top: 2px; }

  .license {
    position: absolute;
    right: 96px;
    top: 184px;
    font-size: 10px;
    font-style: italic;
    color: var(--faint);
  }

  .contact {
    position: absolute;
    right: 80px;
    top: 204px;
    list-style: none;
    text-align: right;
    font-size: 11.5px;
    font-style: italic;
    color: var(--muted);
    line-height: 18px;
    white-space: nowrap;
  }
  .contact li { display: flex; justify-content: flex-end; align-items: center; gap: 8px; }
  .contact li::after {
    content: "";
    width: 6px; height: 6px;
    background: var(--gold);
    transform: rotate(45deg);
  }
</style>
</head>
<body>

  <section class="card card--back">
    <svg class="edge edge--left" viewBox="0 0 40 320" preserveAspectRatio="none" aria-hidden="true">
      <polygon points="0,0 40,0 0,320" fill="var(--brown)"/>
    </svg>
    <div class="brand">
      <span class="brand__mark"></span>
      <span class="brand__name">Bayt Nuwaris</span>
    </div>
  </section>

  <section class="card card--front">
    <div class="brand">
      <span class="brand__mark"></span>
      <span class="brand__name">Bayt Nuwaris</span>
    </div>

    <div class="person">
      <p class="person__name">Fahad Omar Qurashi</p>
      <p class="person__role">Owner</p>
    </div>

    <p class="license">License No.: 4030551208</p>

    <ul class="contact">
      <li>Rawda Street P.O.Box 483920 Jeddah 24719 Saudi Arabia</li>
      <li>Tell: +966125550143 Cell: +966555000198</li>
      <li>Fax: +966125550143 Email: baytnuwaris@mailbox-example.com</li>
    </ul>

    <svg class="edge edge--right" viewBox="0 0 56 320" preserveAspectRatio="none" aria-hidden="true">
      <polygon points="56,0 56,150 20,150" fill="var(--brown)"/>
      <polygon points="20,150 56,150 56,320 0,320" fill="var(--gold)"/>
      <polygon points="20,150 56,150 56,168" fill="var(--gold-dark)"/>
    </svg>
  </section>

</body>
</html>
```